Etiketten für Honiggläser gesucht
sehr kreativer Entwurf, in dem alle umfangreichen Vorgaben berücksichtigt wurden. q4472 ist sehr service- und lösungsorientiert. Arbeitet sehr schnell und exzellent.
Zielgruppe
Wir sind eine junge Hobbyimkerei und produzieren unsere eigenen Honigsorten. Zielgruppe ist jeder, der Honig mag.
Aufgabenstellung
Das zu entwerfende Etiketten_Design soll grundsätzlich ein „absoluter Hingucker“ werden, einen hohen Wiedererkennungswert besitzen, edel erscheinen und die Hochwertigkeit des Produktes zum Ausdruck bringen.
Im engeren Sinn sollen zwei voneinander unabhängige Etikettenteile entworfen werden, die aber im Design eine Einheit bilden sollen:
Beim ersten Teil handelt es sich um den sogenannten Gewährverschluss; er verbindet den Deckel mit dem Glas und zerreißt beim ersten Öffnen des Deckels. Der Gewährverschluss soll etwa 2 cm breit und 8 cm lang sein, und unter anderem von unserem Firmenlogo (siehe Datei) geziert werden. Bei dem Logo darf die Grafik und der Hintergrund in der Farbe variieren, und der Schriftzug kann entfallen, andere Änderungen dürfen jedoch nicht vorgenommen werden. Das Logo kann bei Bedarf gerne in anderen Dateiformaten zur Verfügung gestellt werden.
Den zweiten Teil stellt das eigentliche Produktetikett dar. Für dieses gibt es keine Größen- und Formvorgaben, allerdings müssen folgende Inhalte Berücksichtigung finden: Die Daten des Imkers (bitte folgende Platzhalter verwenden „Firmenname“, „Vorname1 & Vorname2 Nachname“, „Straße + Hausnummer“, „PLZ + Ortsname“, „Internetseite“ und „Emailadresse“) sowie den Angaben „500g“, „Mindestens haltbar bis:“ (dahinter oder darunter bitte weißen Freiraum für den Stempelaufdruck des Datums lassen), „Trocken, dunkel und vor Wärme geschützt lagern!“, und – ganz wichtig – die „Honigsorte“ mit den vorangestellten Worten „feinster deutscher“ (, z.B. „feinster deutscher Rapshonig“).
Jede Honigsorte soll mit einer Farbe verknüpft werden, sodass der Kunde schnell erkennen kann um welche Honigsorte es sich im Glas handelt (beispielsweise gelb für Rapshonig, grün für Waldhonig, usw.). Dafür soll die jeweilige Honigsortenfarbe, in welcher Form auch immer, das Etikett oder einen bestimmten Bereich davon domini..

```html
<!DOCTYPE html>
<html lang="de">
<head>
<meta charset="utf-8">
<title>Imkerei Roderich – Honigetiketten</title>
<link rel="stylesheet" href="https://fonts.googleapis.com/css2?family=Cormorant+SC:wght@500;600&family=Cormorant+Garamond:ital,wght@0,500;1,500&display=swap">
<style>
  :root{
    --board:#e4e5e7;
    --label:#fbf9ec;
    --ink:#3a3a3a;
    --ink-soft:#6b6b66;
    --heide:#9b3c90;
    --himbeer:#b8333d;
    --brombeer:#8e86b9;
    --linden:#a9b3a6;
    --kirsch:#8fa27f;
    --klee:#9dc07a;
    --akazie:#3f9a6b;
    --eiche:#9b7f3c;
  }
  *{box-sizing:border-box;margin:0;padding:0}
  html,body{width:1200px;height:1200px;overflow:hidden}
  body{background:var(--board);font-family:"Cormorant Garamond",Georgia,serif;color:var(--ink);position:relative}

  .brand{position:absolute;left:468px;top:42px;transform:translateX(-50%);text-align:center}
  .brand-dot{width:54px;height:54px;border-radius:50%;border:3px solid var(--ink);margin:0 auto 10px}
  .brand-name{font-family:"Cormorant SC",Georgia,serif;font-weight:600;font-size:34px;letter-spacing:5px;line-height:1}

  .hex-wrap{position:absolute;filter:drop-shadow(0 3px 4px rgba(0,0,0,.22))}
  .hex{width:100%;height:100%;background:var(--label);
    clip-path:polygon(25% 0,75% 0,100% 50%,75% 100%,25% 100%,0 50%);
    display:flex;flex-direction:column;align-items:center;text-align:center}
  .hex-mark{border-radius:50%;border:2px solid var(--ink)}
  .hex-brand{font-family:"Cormorant SC",Georgia,serif;font-weight:600;color:var(--ink);letter-spacing:1px;line-height:1}
  .hex-window{display:block}
  .hex-pre{font-style:italic;color:var(--ink-soft);line-height:1}
  .hex-variety{font-family:"Cormorant SC",Georgia,serif;font-weight:500;line-height:1;letter-spacing:.5px}
  .hex-weight{font-weight:500;line-height:1}

  .label-main{left:413px;top:154px;width:360px;height:312px}
  .label-main .hex{padding-top:18px}
  .label-main .hex-mark{width:22px;height:22px}
  .label-main .hex-brand{font-size:15px;margin-top:5px}
  .label-main .hex-window{width:104px;height:90px;margin-top:10px}
  .label-main .hex-pre{font-size:13px;margin-top:12px}
  .label-main .hex-variety{font-size:30px;color:var(--ink);margin-top:3px}
  .label-main .hex-weight{font-size:15px;margin-top:3px}

  .seal{position:absolute;left:682px;top:14px;width:220px;height:400px;filter:drop-shadow(0 3px 4px rgba(0,0,0,.22))}
  .seal svg{position:absolute;inset:0}
  .seal-mark{position:absolute;left:97px;top:22px;width:26px;height:26px;border-radius:50%;border:2px solid var(--ink)}
  .seal-info{position:absolute;left:30px;top:228px;width:160px;text-align:center;font-size:8.5px;line-height:1.35;color:var(--ink-soft)}
  .seal-info .date{margin-top:6px}
  .seal-info .date-space{height:22px}
  .seal-foot-mark{position:absolute;left:102px;top:352px;width:16px;height:16px;border-radius:50%;border:1.5px solid var(--ink)}

  .range .hex-wrap{width:150px;height:130px}
  .range .hex{padding-top:9px}
  .range .hex-mark{width:13px;height:13px;border-width:1.5px}
  .range .hex-brand{font-size:7.5px;margin-top:3px}
  .range .hex-window{width:44px;height:38px;margin-top:6px}
  .range .hex-pre{font-size:6.5px;margin-top:6px}
  .range .hex-variety{font-size:13px;margin-top:2px}
  .range .hex-weight{font-size:7px;margin-top:2px}

  .more{position:absolute;left:1080px;top:690px;display:flex;gap:7px}
  .more span{width:7px;height:7px;border-radius:50%;background:#8a8a8a}

  .scene{position:absolute;left:0;top:752px;width:1200px;height:448px;
    background:linear-gradient(90deg,#4a3a22 0%,#c78a2a 22%,#e3a93a 45%,#6f8f3e 70%,#2f4f23 100%)}
</style>
</head>
<body>

  <div class="brand">
    <div class="brand-dot"></div>
    <div class="brand-name">Imkerei Roderich</div>
  </div>

  <div class="hex-wrap label-main">
    <div class="hex">
      <span class="hex-mark"></span>
      <span class="hex-brand">Imkerei Roderich</span>
      <svg class="hex-window" viewBox="0 0 104 90"><polygon points="26,4 78,4 100,45 78,86 26,86 4,45" fill="none" stroke="var(--heide)" stroke-width="7"/></svg>
      <span class="hex-pre">feinster deutscher</span>
      <span class="hex-variety" style="color:var(--heide)">Heidehonig</span>
      <span class="hex-weight">500g</span>
    </div>
  </div>

  <div class="seal">
    <svg viewBox="0 0 220 400" width="220" height="400">
      <path fill="var(--label)" d="M85 8 H135 L160 40 L135 72 H122 V212 H160 L210 302 L160 392 H60 L10 302 L60 212 H98 V72 H85 L60 40 Z"/>
    </svg>
    <span class="seal-mark"></span>
    <div class="seal-info">
      <div>Firmenname</div>
      <div>Vorname1 &amp; Vorname2 Nachname</div>
      <div>Straße + Hausnummer</div>
      <div>PLZ + Ortsname</div>
      <div>Internetseite · Emailadresse</div>
      <div class="date">Mindestens haltbar bis:</div>
      <div class="date-space"></div>
      <div>Trocken, dunkel und vor Wärme geschützt lagern!</div>
    </div>
    <span class="seal-foot-mark"></span>
  </div>

  <div class="range">
    <div class="hex-wrap" style="left:98px;top:545px"><div class="hex"><span class="hex-mark"></span><span class="hex-brand">Imkerei Roderich</span><svg class="hex-window" viewBox="0 0 44 38"><polygon points="11,2 33,2 42,19 33,36 11,36 2,19" fill="none" stroke="var(--heide)" stroke-width="3"/></svg><span class="hex-pre">feinster deutscher</span><span class="hex-variety">Heidehonig</span><span class="hex-weight">500g</span></div></div>
    <div class="hex-wrap" style="left:213px;top:560px"><div class="hex"><span class="hex-mark"></span><span class="hex-brand">Imkerei Roderich</span><svg class="hex-window" viewBox="0 0 44 38"><polygon points="11,2 33,2 42,19 33,36 11,36 2,19" fill="none" stroke="var(--himbeer)" stroke-width="3"/></svg><span class="hex-pre">feinster deutscher</span><span class="hex-variety">Himbeerhonig</span><span class="hex-weight">500g</span></div></div>
    <div class="hex-wrap" style="left:328px;top:545px"><div class="hex"><span class="hex-mark"></span><span class="hex-brand">Imkerei Roderich</span><svg class="hex-window" viewBox="0 0 44 38"><polygon points="11,2 33,2 42,19 33,36 11,36 2,19" fill="none" stroke="var(--brombeer)" stroke-width="3"/></svg><span class="hex-pre">feinster deutscher</span><span class="hex-variety">Brombeerhonig</span><span class="hex-weight">500g</span></div></div>
    <div class="hex-wrap" style="left:446px;top:560px"><div class="hex"><span class="hex-mark"></span><span class="hex-brand">Imkerei Roderich</span><svg class="hex-window" viewBox="0 0 44 38"><polygon points="11,2 33,2 42,19 33,36 11,36 2,19" fill="none" stroke="var(--linden)" stroke-width="3"/></svg><span class="hex-pre">feinster deutscher</span><span class="hex-variety">Lindenhonig</span><span class="hex-weight">500g</span></div></div>
    <div class="hex-wrap" style="left:561px;top:545px"><div class="hex"><span class="hex-mark"></span><span class="hex-brand">Imkerei Roderich</span><svg class="hex-window" viewBox="0 0 44 38"><polygon points="11,2 33,2 42,19 33,36 11,36 2,19" fill="none" stroke="var(--kirsch)" stroke-width="3"/></svg><span class="hex-pre">feinster deutscher</span><span class="hex-variety">Kirschhonig</span><span class="hex-weight">500g</span></div></div>
    <div class="hex-wrap" style="left:676px;top:560px"><div class="hex"><span class="hex-mark"></span><span class="hex-brand">Imkerei Roderich</span><svg class="hex-window" viewBox="0 0 44 38"><polygon points="11,2 33,2 42,19 33,36 11,36 2,19" fill="none" stroke="var(--klee)" stroke-width="3"/></svg><span class="hex-pre">feinster deutscher</span><span class="hex-variety">Kleehonig</span><span class="hex-weight">500g</span></div></div>
    <div class="hex-wrap" style="left:789px;top:545px"><div class="hex"><span class="hex-mark"></span><span class="hex-brand">Imkerei Roderich</span><svg class="hex-window" viewBox="0 0 44 38"><polygon points="11,2 33,2 42,19 33,36 11,36 2,19" fill="none" stroke="var(--akazie)" stroke-width="3"/></svg><span class="hex-pre">feinster deutscher</span><span class="hex-variety">Akazienhonig</span><span class="hex-weight">500g</span></div></div>
    <div class="hex-wrap" style="left:904px;top:560px"><div class="hex"><span class="hex-mark"></span><span class="hex-brand">Imkerei Roderich</span><svg class="hex-window" viewBox="0 0 44 38"><polygon points="11,2 33,2 42,19 33,36 11,36 2,19" fill="none" stroke="var(--eiche)" stroke-width="3"/></svg><span class="hex-pre">feinster deutscher</span><span class="hex-variety">Eichenhonig</span><span class="hex-weight">500g</span></div></div>
  </div>

  <div class="more"><span></span><span></span><span></span></div>

  <div class="scene" role="img" aria-label="Foto: Honiggläser mit den Etiketten auf einem Holztisch neben einer Bienenwabe im Garten"></div>

</body>
</html>
```